Corporate Design für Onlineshop zum Verkauf von asiatischen Reflexbögen
Ein tolles Design und hervorragende Zusammenarbeit! Alle unsere Sonderwünsche wurden einwandfrei umgesetzt. Ich kann Vrelmo aus vollstem Herzen empfehlen. Unser Gewinner!
Zielgruppe
Ich bin Einzelunternehmer (Marwend Bogensport Helmut Drabeck) und verkaufe in meinem Webshop Asiatische Reflexbögen, häufig auch als Reiterbögen bezeichnet, und alles was der traditionelle Bogenschütze so braucht (z.B. Pfeile, Köcher, Zubehör, etc...)
Aufgabenstellung
Ich suche ein einprägsames Design, das in verschiedenen Größen gut funktioniert und erkennbar ist (sowohl als kleines Logo als auch größer auf Messeständen oder Flyern).
Das Logo sollte am Besten sowohl farbig (z.B. Onlineshop, Visitenkarte, Briefkopf) als auch schwarz/weiß (z.B. als Gravur auf Leder oder Holz) funktionieren.
Wenn die Silouhette eines gespannten typischen Reiterbogens (tatarisch, mongolisch, skytisch oder chinesisch) im Logo drin wäre und ein stilisierter Fuchs, dann würde das den Namen villeicht ganz gut untermalen glaub ich.
Meine Hauptkunden sind Bogenschützen, die vornehmlich mit traditionellen Bögen schießen, sowohl auf dem Platz als auch in der Natur auf dem 3D-Parcours.
Der Name MarWend leitet sich von 'fux = Fuchs' und 'luoga = versteckter Wohnung' ab, heißt also in etwa 'Fuchsbau' so sind hier im Süddeutschen und Österreichischen einige Ortsteile bzw. Einöden benannt, z.B. Marwend oder Fuchslug in Aschau im Chiemgau.
Meinen Onlineshop baue ich gerade auf, da ist also noch nicht wirklich was zu sehen. Ich brauche daher ein Logo für Shop, Visitenkarte und Briefpapier und ein Design für Visitenkarte und ein Design für Briefpapier/Rechnungen.

```html
<!DOCTYPE html>
<html lang="de">
<head>
<meta charset="utf-8">
<title>Marwend Bogensport – Visitenkarte</title>
<link rel="stylesheet" href="https://fonts.googleapis.com/css2?family=Montserrat:wght@400;500;700&display=swap">
<style>
  :root {
    --page: #ffffff;
    --card: #ffffff;
    --ink: #2f2f2f;
    --ink-soft: #6a6a6a;
    --accent: #f39200;
    --accent-pale: #fbe6c6;
    --grey-pale: #e4e4e4;
    --card-edge: #e2e2e2;
  }
  * { box-sizing: border-box; margin: 0; padding: 0; }
  html, body {
    width: 1200px; height: 675px; overflow: hidden;
    background: var(--page);
    font-family: "Montserrat", sans-serif;
    color: var(--ink);
  }
  .canvas { position: relative; width: 1200px; height: 675px; }

  .card {
    position: absolute;
    width: 500px; height: 324px;
    background: var(--card);
    border: 1px solid var(--card-edge);
    box-shadow: 0 6px 18px rgba(0,0,0,.12);
    overflow: hidden;
  }
  .card--contact { left: 70px; top: 70px; }
  .card--brand { left: 630px; top: 70px; }

  /* Contact side */
  .name-block {
    position: absolute; left: 0; top: 138px;
    display: flex; align-items: center;
  }
  .name-block__bar { width: 56px; height: 28px; background: var(--accent); }
  .name-block__text { padding-left: 14px; }
  .person-name { font-weight: 700; font-size: 19px; letter-spacing: .2px; }
  .person-role { font-size: 11px; color: var(--ink-soft); margin-top: 3px; }

  .divider {
    position: absolute; left: 262px; top: 92px;
    width: 2px; height: 142px; background: var(--accent);
  }
  .contact-list {
    position: absolute; left: 280px; top: 96px;
    list-style: none; font-size: 11px; line-height: 1.45; color: var(--ink);
  }
  .contact-list li { display: flex; align-items: flex-start; gap: 8px; margin-bottom: 5px; }
  .contact-list svg { width: 12px; height: 12px; flex: none; margin-top: 2px; }

  .decor-corner {
    position: absolute; right: -30px; top: -40px;
    width: 220px; height: 130px;
    background: linear-gradient(135deg, var(--grey-pale), var(--accent-pale));
    opacity: .55;
  }

  /* Brand side */
  .decor-large {
    position: absolute; left: 90px; top: 30px;
    width: 320px; height: 264px;
    background: radial-gradient(circle at 50% 45%, var(--accent-pale), var(--grey-pale) 70%);
    opacity: .6;
  }
  .brand-lockup {
    position: absolute; left: 0; right: 0; top: 138px;
    display: flex; align-items: center; justify-content: center; gap: 12px;
  }
  .brand-mark { width: 18px; height: 18px; background: var(--accent); }
  .brand-name {
    font-weight: 500; font-size: 36px; letter-spacing: 7px; color: var(--ink);
  }

  /* Standalone lockup */
  .logo-lockup {
    position: absolute; left: 70px; top: 470px;
    display: flex; align-items: center; gap: 16px;
  }
  .logo-lockup .brand-mark { width: 30px; height: 30px; }
  .logo-lockup .brand-name { font-size: 58px; letter-spacing: 10px; }
</style>
</head>
<body>
<main class="canvas">

  <section class="card card--contact">
    <div class="decor-corner" role="img" aria-label="Faint decorative brand symbol in grey and pale orange"></div>

    <div class="name-block">
      <div class="name-block__bar"></div>
      <div class="name-block__text">
        <p class="person-name">Jonas Kerber</p>
        <p class="person-role">Inhaber</p>
      </div>
    </div>

    <div class="divider"></div>

    <ul class="contact-list">
      <li>
        <svg viewBox="0 0 12 12" aria-hidden="true"><path d="M6 0.5a3.8 3.8 0 0 0-3.8 3.8C2.2 7.2 6 11.5 6 11.5s3.8-4.3 3.8-7.2A3.8 3.8 0 0 0 6 0.5zm0 5.2a1.4 1.4 0 1 1 0-2.8 1.4 1.4 0 0 1 0 2.8z" fill="var(--accent)"/></svg>
        <span>Lindenweg 4<br>83229 Talbach</span>
      </li>
      <li>
        <svg viewBox="0 0 12 12" aria-hidden="true"><path d="M2.6 1l2 2.2-1 1.3a7 7 0 0 0 3.9 3.9l1.3-1 2.2 2-1.3 1.6C5 10.6 1.4 7 .9 2.3z" fill="var(--accent)"/></svg>
        <span>030 518204 716</span>
      </li>
      <li>
        <svg viewBox="0 0 12 12" aria-hidden="true"><rect x="3" y="0.5" width="6" height="11" rx="1.2" fill="none" stroke="var(--accent)" stroke-width="1.2"/><circle cx="6" cy="9.6" r=".7" fill="var(--accent)"/></svg>
        <span>0171 642 80 315</span>
      </li>
      <li>
        <svg viewBox="0 0 12 12" aria-hidden="true"><rect x="0.8" y="2.3" width="10.4" height="7.4" rx="1" fill="none" stroke="var(--accent)" stroke-width="1.2"/><path d="M1 2.8l5 3.8 5-3.8" fill="none" stroke="var(--accent)" stroke-width="1.2"/></svg>
        <span>kontakt@marwend.de</span>
      </li>
      <li>
        <svg viewBox="0 0 12 12" aria-hidden="true"><circle cx="6" cy="6" r="5.2" fill="none" stroke="var(--accent)" stroke-width="1.1"/><ellipse cx="6" cy="6" rx="2.2" ry="5.2" fill="none" stroke="var(--accent)" stroke-width="1"/><path d="M.8 6h10.4" stroke="var(--accent)" stroke-width="1"/></svg>
        <span>www.marwend.de</span>
      </li>
    </ul>
  </section>

  <section class="card card--brand">
    <div class="decor-large" role="img" aria-label="Large faint decorative brand symbol in grey and pale orange"></div>
    <div class="brand-lockup">
      <span class="brand-mark"></span>
      <span class="brand-name">MARWEND</span>
    </div>
  </section>

  <div class="logo-lockup">
    <span class="brand-mark"></span>
    <span class="brand-name">MARWEND</span>
  </div>

</main>
</body>
</html>
```